Business Card Design Project - veltramo

We are building an agency for innovative solutions in marketing, education and events to pharmaceutical companies, physicians, medical societies, patient advocacy groups. We want to become a reference in this market in Brazil as the most boutique agency here. We deal with every detail with a lot of love and caring for what we do like craftsmen.
Our card must show innovation and inspiration. Yet should be clean. Something like Swiss design, quince design, etc.
Updates
Reason: I think the initial time was too short. I believe with more time you can exceed expectations. I'm liking a lot this experience
Target Market(s)
Pharmaceutical companies, doctors and patients
Industry/Entity Type
Pharmaceutical
Font styles to use
Other font styles liked:
- Helvetia family
Colors
Designer to choose colors to be used in the design.
Requirements
Must have
- Modern, clean,
Nice to have
- Innovative idea to show
Should not have
- Not too appear too much Comercial. Must be modern but sober.

```html
<!DOCTYPE html>
<html lang="en">
<head>
<meta charset="utf-8">
<title>veltramo business card</title>
<link rel="stylesheet" href="https://fonts.googleapis.com/css2?family=Arimo:wght@400;500&family=Roboto+Slab:wght@500&display=swap">
<style>
  :root {
    --bg: #d9d6d0;
    --ink: #000000;
    --paper: #ffffff;
    --green: #7cc242;
    --blue: #2f78c4;
    --text-dark: #111111;
  }
  * { margin: 0; padding: 0; box-sizing: border-box; }
  html, body { width: 1200px; height: 800px; overflow: hidden; }
  body {
    background: var(--bg);
    display: flex;
    align-items: center;
    justify-content: center;
    gap: 40px;
    font-family: "Arimo", Helvetica, Arial, sans-serif;
  }
  .card {
    position: relative;
    width: 540px;
    height: 309px;
    overflow: hidden;
    box-shadow: 0 6px 18px rgba(0,0,0,0.18);
  }

  /* Front */
  .card-front { background: var(--paper); }
  .card-front .band {
    position: absolute;
    left: 0; right: 0;
    top: 52px; bottom: 68px;
    background: var(--ink);
    display: flex;
    align-items: center;
    justify-content: center;
  }

  .wordmark {
    font-family: "Arimo", Helvetica, Arial, sans-serif;
    font-weight: 400;
    color: var(--green);
    letter-spacing: 0.5px;
    line-height: 1;
  }
  .card-front .wordmark { font-size: 52px; }

  /* Back */
  .card-back { background: var(--ink); }
  .card-back .contact-panel {
    position: absolute;
    top: 0; right: 0;
    width: 232px;
    height: 168px;
    background: var(--paper);
    padding: 26px 0 0 30px;
    color: var(--text-dark);
    font-size: 13.5px;
    line-height: 1.2;
  }
  .contact-panel .phone { margin-bottom: 14px; }
  .contact-panel .address { margin-bottom: 14px; }
  .card-back .identity {
    position: absolute;
    right: 250px;
    top: 26px;
    text-align: right;
    font-family: "Roboto Slab", Georgia, serif;
    font-weight: 500;
  }
  .identity .person-name { color: var(--green); font-size: 22px; line-height: 1.05; }
  .identity .person-role { color: var(--blue); font-size: 15px; line-height: 1.2; }
  .card-back .wordmark {
    position: absolute;
    left: 40px;
    bottom: 64px;
    font-size: 46px;
  }
</style>
</head>
<body>
  <section class="card card-front" aria-label="Card front">
    <div class="band">
      <span class="wordmark">veltramo</span>
    </div>
  </section>

  <section class="card card-back" aria-label="Card back">
    <div class="identity">
      <p class="person-name">Rafael Quintas</p>
      <p class="person-role">Project Manager</p>
    </div>
    <div class="contact-panel">
      <p class="phone">+55 (11) 3948 207</p>
      <p class="address">48 Rua Alvorada, Vila Serena,<br>SP 04512<br>Caixa Postal: 587203</p>
      <p class="email">ola@veltramo.com</p>
    </div>
    <span class="wordmark">veltramo</span>
  </section>
</body>
</html>
```